Business Card Design Project

Velvet Harbor is a Boutique Clothing. On the business cards I would like to have this included
Website: www.velvetharbor-example.com
Email: shop@velvetharbor-example.com
Owner: Mira Sol & Tor Dell

Industry/Entity Type

Business

Contact Information for Business Card

I wanted something simple and elegant. I have attach business logo.

```html
<!DOCTYPE html>
<html lang="en">
<head>
<meta charset="utf-8">
<title>Velvet Harbor Business Cards</title>
<link href="https://fonts.googleapis.com/css2?family=Lato:wght@400;700&display=swap" rel="stylesheet">
<style>
  :root {
    --ink: #2b2b2b;
    --paper: #ffffff;
    --stage: #ece9e6;
    --soft-text: #e9e9e9;
  }
  * { margin: 0; padding: 0; box-sizing: border-box; }
  html, body { width: 1200px; height: 900px; overflow: hidden; }
  body {
    background: var(--stage);
    font-family: "Lato", Arial, sans-serif;
    position: relative;
  }
  .card {
    position: absolute;
    overflow: hidden;
    box-shadow: 0 6px 18px rgba(0,0,0,0.18);
  }
  .card--front {
    left: 178px; top: 74px; width: 588px; height: 364px;
    background: var(--ink);
  }
  .card--back {
    left: 388px; top: 505px; width: 567px; height: 352px;
    background: var(--paper);
  }
  .band { position: absolute; left: 0; width: 100%; }
  .card--front .band { top: 74px; height: 90px; background: var(--paper); }
  .card--back .band { top: 132px; height: 86px; background: var(--ink); }
  .seal {
    position: absolute;
    border-radius: 50%;
    display: flex; align-items: center; justify-content: center;
    text-align: center;
  }
  .card--front .seal {
    left: 196px; top: 21px; width: 194px; height: 194px;
    background: var(--paper);
  }
  .card--back .seal {
    left: 200px; top: 82px; width: 186px; height: 186px;
    background: var(--ink);
  }
  .brand-name {
    font-weight: 400;
    font-size: 22px;
    letter-spacing: 4px;
    line-height: 1.35;
    text-transform: uppercase;
  }
  .card--front .brand-name { color: var(--ink); }
  .card--back .brand-name { color: var(--soft-text); }
  .contact {
    position: absolute; left: 0; top: 240px; width: 100%;
    text-align: center; color: var(--paper);
  }
  .owners { font-weight: 700; font-size: 19px; letter-spacing: 0.3px; }
  .role { font-size: 14px; margin-top: 4px; letter-spacing: 0.5px; }
  .email, .website { font-size: 16px; }
  .email { margin-top: 12px; }
  .website { margin-top: 2px; }
</style>
</head>
<body>
  <section class="card card--front">
    <div class="band"></div>
    <div class="seal"><span class="brand-name">Velvet<br>Harbor</span></div>
    <div class="contact">
      <p class="owners">MIRA SOL &amp; TOR DELL</p>
      <p class="role">OWNER</p>
      <p class="email">shop@velvetharbor-example.com</p>
      <p class="website">www.velvetharbor-example.com</p>
    </div>
  </section>

  <section class="card card--back">
    <div class="band"></div>
    <div class="seal"><span class="brand-name">Velvet<br>Harbor</span></div>
  </section>
</body>
</html>
```